Professional Sales Business looking for inspirational poster

I need an inspirational poster design for sales professionals, targeted around the phrase "Win Fast, Lose Fast". The style of the poster will be primarily minimalistic and flat with the main focus being on the phrase, however, any graphics or creative font and background styles are encouraged. Color choice is up to you.

Design Specs:
Vector files are best. If creating a vector file isn't possible, 150dpi raster images (at actual size or bigger) are good too. The poster must be in a portrait layout and scalable to the sizes of 18" X 24" and 24" X 36". Please convert all text to outlines.

Please msg me if you have any additional questions.

```html
<!DOCTYPE html>
<html lang="en">
<head>
<meta charset="utf-8">
<title>Win Fast Lose Fast — Sales Poster</title>
<link rel="stylesheet" href="https://fonts.googleapis.com/css2?family=Anton&display=swap">
<style>
  :root {
    --bg-core: #c940bc;
    --bg-edge: #8e1689;
    --word-light: #fdb4f5;
    --word-dark: #5c0a55;
    --word-shadow: rgba(60, 0, 55, 0.35);
  }
  html, body {
    margin: 0;
    padding: 0;
    width: 800px;
    height: 1200px;
    overflow: hidden;
  }
  .poster {
    position: relative;
    width: 800px;
    height: 1200px;
    background:
      radial-gradient(ellipse 75% 65% at 45% 50%, var(--bg-core) 55%, var(--bg-edge) 130%);
    overflow: hidden;
  }
  .slogan {
    position: absolute;
    inset: 0;
    width: 800px;
    height: 1200px;
  }
  .slogan text {
    font-family: "Anton", "Oswald", sans-serif;
    text-transform: uppercase;
  }
  .word-light {
    fill: var(--word-light);
    filter: drop-shadow(2px 3px 3px var(--word-shadow));
  }
  .word-dark {
    fill: var(--word-dark);
  }
</style>
</head>
<body>
  <main class="poster">
    <svg class="slogan" viewBox="0 0 800 1200" role="img" aria-label="Win fast, lose fast">
      <text class="word-light word-win" x="350" y="383" font-size="172"
            textLength="316" lengthAdjust="spacingAndGlyphs"
            transform="rotate(-4 508 310)">Win</text>
      <text class="word-dark word-fast" x="362" y="546" font-size="166"
            textLength="348" lengthAdjust="spacingAndGlyphs">Fast</text>
      <text class="word-light word-lose" x="360" y="722" font-size="150"
            textLength="354" lengthAdjust="spacingAndGlyphs"
            transform="rotate(-3 537 658)">Lose</text>
      <text class="word-dark word-fast" x="362" y="894" font-size="166"
            textLength="348" lengthAdjust="spacingAndGlyphs">Fast</text>
    </svg>
  </main>
</body>
</html>
```